Generic Business Card

I need a business card for my new cafe which is only six weeks old. I'm continuously asked for a business so that customers can either keep or pass on to a friend. I'd also like a card that I can give out with each bill which contains the business name, address, contact details and website.
The cafe's internal design has an industrial feel to it with modern subdued colours. I have attached an internal photo along with my main hero shot and logo.
The hero shot features prominently on my website and other print material and I would also like it to appear on my bus card.

Target Market(s)

Men & women between 35 and 45 years of age who know and enjoy good coffee.

Industry/Entity Type

Industrial

Contact Information for Business Card

Shop 7b/118-120 Pelbourne Street, East Dalvington 3981
Tel. 9462 3157
www.talvemo.com.au

```html
<!DOCTYPE html>
<html lang="en">
<head>
<meta charset="utf-8">
<title>Talvemo Business Card</title>
<link rel="stylesheet" href="https://fonts.googleapis.com/css2?family=Questrial&display=swap">
<style>
  :root {
    --backdrop: #3a3a3a;
    --card: #e7e7e8;
    --band: #a7a7a9;
    --ink: #1f1f1f;
    --leaf: #8cc63f;
  }
  html, body {
    margin: 0;
    padding: 0;
    width: 1200px;
    height: 736px;
    overflow: hidden;
    background: var(--backdrop);
    font-family: "Questrial", "Century Gothic", sans-serif;
  }
  .card {
    position: absolute;
    left: 120px;
    top: 74px;
    width: 960px;
    height: 588px;
    background: var(--card);
    border-radius: 40px;
    overflow: hidden;
    color: var(--ink);
  }
  .brand-band {
    position: absolute;
    left: 0;
    top: 70px;
    width: 700px;
    height: 200px;
    background: var(--band);
    border-radius: 0 100px 100px 0;
  }
  .brand {
    position: absolute;
    left: 150px;
    top: 118px;
    display: flex;
    align-items: center;
    gap: 22px;
  }
  .brand-dot {
    width: 58px;
    height: 58px;
    border-radius: 50%;
    background: var(--leaf);
  }
  .brand-name {
    font-size: 92px;
    line-height: 1;
    letter-spacing: 4px;
    text-transform: uppercase;
    color: var(--ink);
  }
  .address {
    position: absolute;
    right: 530px;
    top: 318px;
    margin: 0;
    font-style: normal;
    font-size: 29px;
    line-height: 40px;
    text-align: right;
  }
  .divider {
    position: absolute;
    left: 450px;
    top: 312px;
    width: 2px;
    height: 140px;
    background: var(--ink);
  }
  .contact {
    position: absolute;
    left: 472px;
    top: 372px;
    margin: 0;
    padding: 0;
    list-style: none;
    font-size: 29px;
    line-height: 40px;
  }
  .contact li {
    display: flex;
    align-items: center;
    gap: 6px;
  }
  .contact svg {
    width: 22px;
    height: 22px;
    flex: none;
  }
</style>
</head>
<body>
  <section class="card" aria-label="Talvemo business card">
    <div class="brand-band"></div>
    <div class="brand">
      <span class="brand-dot"></span>
      <span class="brand-name">Talvemo</span>
    </div>

    <address class="address">
      Shop 7b/118-120<br>
      Pelbourne Street<br>
      East Dalvington 3981
    </address>

    <div class="divider"></div>

    <ul class="contact">
      <li>
        <svg viewBox="0 0 24 24" aria-hidden="true">
          <circle cx="12" cy="12" r="10.5" fill="none" stroke="#1f1f1f" stroke-width="1.6"/>
          <path d="M8.5 7.5c.6-.6 1.4-.5 1.8.1l1 1.5c.3.5.2 1.1-.2 1.5l-.6.5c.6 1.2 1.5 2.1 2.7 2.7l.5-.6c.4-.4 1-.5 1.5-.2l1.5 1c.6.4.7 1.2.1 1.8l-.7.7c-.8.8-2.1.9-3.1.3-2.3-1.3-4-3-5.3-5.3-.6-1-.5-2.3.3-3.1z" fill="#1f1f1f"/>
        </svg>
        <span>9462 3157</span>
      </li>
      <li>
        <svg viewBox="0 0 24 24" aria-hidden="true">
          <circle cx="12" cy="12" r="10.5" fill="none" stroke="#1f1f1f" stroke-width="1.6"/>
          <circle cx="12" cy="12" r="6" fill="none" stroke="#1f1f1f" stroke-width="1.3"/>
          <ellipse cx="12" cy="12" rx="2.6" ry="6" fill="none" stroke="#1f1f1f" stroke-width="1.1"/>
          <line x1="6" y1="12" x2="18" y2="12" stroke="#1f1f1f" stroke-width="1.1"/>
        </svg>
        <span>www.talvemo.com.au</span>
      </li>
    </ul>
  </section>
</body>
</html>
```